Employees at R&T Gale Power Services need new modern business cards

We need new business cards that showcase our new rebranded logo. We are seeking modern, clean, fresh, attractive cards while still being professional. We want to stand out. A little bit about us: we work in Canada and the USA. We offer Technical Field Advisors to support wind turbine manufacturers through the construction phase of wind farms. I am attaching a mock inspiration picture to lead you in the direction we want to see this go. Also, FYI We have approx. 10/11 different employees that would need their own card. Let me know when you would need everyone's name. We would love to see some black and white options as well as color copies- when using colors we want green to be the dominant color with accents for blue and orange (colors should match our logo). I have also attached copies of our old business card for reference.

Contact Information for Business Card

Name, Telephone, Email, address, company name, website. EXAMPLE: Dean Whitlock, DeanWhitlock@randtgale.net, 555-384-9162, 318276 Fallow Line #7, Marrowby, ON X9Z 4Q2, www.randtgale.net

Colors
0054AA
0677BA
7BADD7
CADEEF
E8F1F8
00AB8E
00BBA5
67D7C9
C6EFE9
E9F9F6
F0912C
F2A743
F7CA91
FBE8D2
FDF5EE

Requirements
Must have
• 2 sided business card

```html
<!DOCTYPE html>
<html lang="en">
<head>
<meta charset="utf-8">
<title>R&amp;T Gale Power Services – Business Card</title>
<link rel="stylesheet" href="https://fonts.googleapis.com/css2?family=Roboto:wght@400;500;700&family=Roboto+Condensed:wght@700&display=swap">
<style>
  :root {
    --page-bg: #efece6;
    --blue-deep: #0567b4;
    --blue-mid: #0677ba;
    --blue-light: #1a9ade;
    --green: #3bb54a;
    --green-text: #35a944;
    --orange: #f2a21f;
    --white: #ffffff;
    --wash-blue: #cadeef;
    --wash-green: #e2f3e4;
    --wash-orange: #fbe8d2;
  }
  * { margin: 0; padding: 0; box-sizing: border-box; }
  html, body {
    width: 1200px; height: 1200px; overflow: hidden;
    background: var(--page-bg);
    font-family: "Roboto", Arial, sans-serif;
  }
  .card {
    position: absolute; left: 280px; width: 640px; height: 367px;
    border-radius: 16px; overflow: hidden;
    box-shadow: 0 2px 4px rgba(0,0,0,0.18);
  }
  .card-front { top: 195px; }
  .card-back { top: 640px; background: var(--green); }
  .card-art { position: absolute; inset: 0; }
  .contact {
    position: absolute; left: 33px; top: 100px; color: var(--white);
  }
  .contact-name {
    font-family: "Roboto Condensed", "Arial Narrow", sans-serif;
    font-weight: 700; font-size: 24px; letter-spacing: 0.2px; line-height: 1;
  }
  .contact-title { font-size: 15px; margin-top: 6px; }
  .contact-list { list-style: none; margin-top: 14px; font-size: 14.5px; }
  .contact-list li { position: relative; padding-left: 19px; line-height: 18px; }
  .contact-list li + li { margin-top: 0; }
  .contact-list .gap { margin-top: 10px; }
  .contact-list svg { position: absolute; left: 0; top: 3px; width: 11px; height: 11px; fill: var(--white); }
  .brand-front {
    position: absolute; left: 330px; top: 210px; width: 270px; text-align: center;
    color: var(--green-text); font-weight: 700; line-height: 1.05;
  }
  .brand-front .brand-line-1 { font-size: 26px; letter-spacing: 2px; }
  .brand-front .brand-line-2 { font-size: 13px; letter-spacing: 3px; }
  .brand-back {
    position: absolute; left: 0; right: 0; top: 240px; text-align: center;
    color: var(--white); font-weight: 700; line-height: 1.05;
  }
  .brand-back .brand-line-1 { font-size: 38px; letter-spacing: 3px; }
  .brand-back .brand-line-2 { font-size: 18px; letter-spacing: 4.5px; }
  .brand-mark { position: absolute; border-radius: 50%; }
  .brand-mark-front { left: 434px; top: 108px; width: 62px; height: 62px; border: 5px solid var(--green-text); }
  .brand-mark-back { left: 250px; top: 77px; width: 140px; height: 140px; border: 8px solid var(--white); }
</style>
</head>
<body>

<section class="card card-front" aria-label="Business card front">
  <svg class="card-art" viewBox="0 0 640 367" width="640" height="367" aria-hidden="true">
    <defs>
      <radialGradient id="blue-glow" cx="0.32" cy="0.45" r="0.75">
        <stop offset="0" stop-color="#1ca0e2"/>
        <stop offset="1" stop-color="#0567b4"/>
      </radialGradient>
      <radialGradient id="soft-wash" cx="0.5" cy="0.5" r="0.5">
        <stop offset="0" stop-color="#ffffff"/>
        <stop offset="0.55" stop-color="#eef5fb"/>
        <stop offset="1" stop-color="#e6f3e8"/>
      </radialGradient>
    </defs>
    <rect width="640" height="367" fill="url(#blue-glow)"/>
    <circle cx="482" cy="178" r="214" fill="var(--white)"/>
    <circle cx="486" cy="176" r="210" fill="var(--orange)"/>
    <circle cx="490" cy="184" r="206" fill="var(--white)"/>
    <circle cx="486" cy="188" r="203" fill="var(--green)"/>
    <circle cx="494" cy="188" r="196" fill="var(--white)"/>
    <ellipse cx="470" cy="190" rx="180" ry="175" fill="url(#soft-wash)" opacity="0.8"
      role="img" aria-label="Faint wind turbine decoration"/>
  </svg>

  <div class="contact">
    <h1 class="contact-name">DEAN WHITLOCK</h1>
    <p class="contact-title">Owner &amp; CEO</p>
    <ul class="contact-list">
      <li><svg viewBox="0 0 12 12"><path d="M6 0a4 4 0 0 0-4 4c0 3 4 8 4 8s4-5 4-8a4 4 0 0 0-4-4zm0 5.6A1.6 1.6 0 1 1 6 2.4a1.6 1.6 0 0 1 0 3.2z"/></svg>318276 Fallow Line #7</li>
      <li>Marrowby, ON X9Z 4Q2</li>
      <li class="gap"><svg viewBox="0 0 12 12"><path d="M2.5 0.5l2 2.3-1 1.4c.8 1.7 2 2.9 3.7 3.7l1.4-1 2.3 2-1 2.1C5 10.8 1.2 7 .4 1.5z"/></svg>555-384-9162</li>
      <li><svg viewBox="0 0 12 12"><path d="M0 2h12v1L6 6.6 0 3zm0 2.3l6 3.6 6-3.6V10H0z"/></svg>DeanWhitlock@randtgale.net</li>
      <li><svg viewBox="0 0 12 12"><path d="M6 0a6 6 0 1 0 0 12A6 6 0 0 0 6 0zm0 1.2c.6 0 1.4 1.3 1.7 3.3H4.3C4.6 2.5 5.4 1.2 6 1.2zM1.3 5.5h2.9c0 .4 0 .8.1 1.2H1.3a4.8 4.8 0 0 1 0-1.2zm.4 2.3h2.7c.2.9.5 1.7.9 2.4a4.8 4.8 0 0 1-3.6-2.4zm6 2.4c.4-.7.7-1.5.9-2.4h2.7a4.8 4.8 0 0 1-3.6 2.4zM7.8 6.7c0-.4.1-.8.1-1.2h2.9a4.8 4.8 0 0 1 0 1.2z"/></svg>www.randtgale.net</li>
    </ul>
  </div>

  <span class="brand-mark brand-mark-front" aria-hidden="true"></span>
  <div class="brand-front">
    <div class="brand-line-1">R&amp;T GALE</div>
    <div class="brand-line-2">POWER SERVICES</div>
  </div>
</section>

<section class="card card-back" aria-label="Business card back">
  <span class="brand-mark brand-mark-back" aria-hidden="true"></span>
  <div class="brand-back">
    <div class="brand-line-1">R&amp;T GALE</div>
    <div class="brand-line-2">POWER SERVICES</div>
  </div>
</section>

</body>
</html>
```